Loomvista: fashion design product software needs your help

Fashion design product software company requests your assistance in designing a complete stationary package around our new logo design. Our software assists fashion designers and apparel houses with efficient communication and streamlined production between each other and manufacturers throughout the entire project design life cycle.

The look should reflect clean, simple and modern design. Not too "techie." Must use the provided logo and colors (or variations on the chosen colors, i.e. percentages as needed).

Reference website: www.loomvista-example.com

Buzzwords: manufacturing, production, apparel design/ers, streamlined process, effective communication, business, production software.

Please try to tone down or make the colors more subtle with more simple design style, layout. No sewing  theme. Thank you.

Target Market(s)

fashion designers and apparel houses that use software to manage and track production process life cycle.

Industry/Entity Type

Communication

Requirements
Must have
• Use of the logo and colors-or variations of colors (attached)
Nice to have
• Playfulness but corporate: with a sense of practicality, economical, streamlined production. Embossing considered.
Should not have
• Please keep in mind economics both financially and economically. Save trees and money! We believe in tactile paper but not "fashion-y" or sparkly, over-the-top colors, effects or production.

```html
<!DOCTYPE html>
<html lang="en">
<head>
<meta charset="utf-8">
<title>Loomvista Stationery Package</title>
<link rel="stylesheet" href="https://fonts.googleapis.com/css2?family=Nunito:wght@800&family=Nunito+Sans:wght@400&display=swap">
<style>
  :root {
    --ink-brown: #5b3325;
    --sky-blue: #2db4e3;
    --paper: #ffffff;
    --backdrop: #000000;
    --body-text: #6b4a3e;
  }
  * { box-sizing: border-box; margin: 0; padding: 0; }
  html, body { width: 1200px; height: 790px; overflow: hidden; background: var(--backdrop); }
  .sheet-set { position: relative; width: 1200px; height: 790px; background: var(--backdrop); }
  .piece { position: absolute; background: var(--paper); overflow: hidden; }
  .piece svg.shape { position: absolute; inset: 0; width: 100%; height: 100%; }
  .fill-brown { fill: var(--ink-brown); }
  .fill-blue { fill: var(--sky-blue); }

  .wordmark {
    position: absolute; display: flex; align-items: center; gap: 5px;
    font-family: "Nunito", "Arial Rounded MT Bold", sans-serif; font-weight: 800;
    color: var(--ink-brown); letter-spacing: -0.3px; line-height: 1;
  }
  .wordmark .dot { width: 9px; height: 9px; border-radius: 50%; background: var(--sky-blue); }
  .wordmark.on-dark { color: var(--paper); }
  .wordmark.on-dark .dot { background: var(--paper); }

  .contact {
    position: absolute; font-family: "Nunito Sans", Arial, sans-serif;
    font-size: 7.5px; line-height: 1.45; color: var(--body-text);
  }
  .contact.on-blue { color: var(--paper); }

  /* business card front */
  .card-front { left: 52px; top: 24px; width: 228px; height: 132px; }
  .card-front .wordmark { left: 18px; top: 84px; font-size: 19px; }
  /* business card back */
  .card-back { left: 296px; top: 24px; width: 256px; height: 132px; }
  .card-back .wordmark { left: 14px; top: 22px; font-size: 16px; }
  .card-back .address { left: 142px; top: 12px; font-size: 6px; }
  .card-back .email { left: 14px; top: 112px; font-size: 6px; }
  /* envelope front */
  .envelope-front { left: 52px; top: 180px; width: 560px; height: 280px; }
  .envelope-front .wordmark { left: 20px; top: 26px; font-size: 20px; }
  .envelope-front .address { left: 444px; top: 20px; }
  .envelope-front .email { left: 44px; top: 244px; }
  /* envelope back */
  .envelope-back { left: 52px; top: 480px; width: 560px; height: 280px; }
  .envelope-back .wordmark { left: 50%; top: 34px; transform: translateX(-50%); font-size: 21px; }
  /* letterhead */
  .letterhead { left: 644px; top: 12px; width: 540px; height: 754px; }
  .letterhead .wordmark { left: 50%; top: 30px; transform: translateX(-50%); font-size: 20px; }
  .letterhead .address { left: 18px; top: 720px; }
  .letterhead .reach { left: 226px; top: 720px; }
</style>
</head>
<body>
<main class="sheet-set">

  <section class="piece card-front" aria-label="Business card front">
    <svg class="shape" viewBox="0 0 228 132" preserveAspectRatio="none" aria-hidden="true">
      <rect class="fill-blue" width="228" height="132"/>
      <path class="fill-brown" d="M0,62 Q110,8 228,22 L228,132 L0,132 Z" stroke="#ffffff" stroke-width="5"/>
    </svg>
    <div class="wordmark on-dark">Loomvista<span class="dot"></span></div>
  </section>

  <section class="piece card-back" aria-label="Business card back">
    <svg class="shape" viewBox="0 0 256 132" preserveAspectRatio="none" aria-hidden="true">
      <path class="fill-blue" d="M0,66 Q128,128 256,66 L256,132 L0,132 Z"/>
      <path d="M0,66 Q128,128 256,66" fill="none" stroke="var(--ink-brown)" stroke-width="3"/>
    </svg>
    <div class="wordmark">Loomvista<span class="dot"></span></div>
    <p class="contact address">248 Mercer Street<br>Brooklyn, NY 11201<br>646-555-0142</p>
    <p class="contact on-blue email">contact@loomvista-example.com</p>
  </section>

  <section class="piece envelope-front" aria-label="Envelope front">
    <svg class="shape" viewBox="0 0 560 280" preserveAspectRatio="none" aria-hidden="true">
      <path class="fill-blue" d="M0,160 Q280,230 560,166 L560,280 L0,280 Z"/>
      <path d="M0,160 Q280,230 560,166" fill="none" stroke="var(--ink-brown)" stroke-width="5"/>
    </svg>
    <div class="wordmark">Loomvista<span class="dot"></span></div>
    <p class="contact address">248 Mercer Street<br>Brooklyn, NY 11201<br>646-555-0142</p>
    <p class="contact on-blue email">contact@loomvista-example.com</p>
  </section>

  <section class="piece envelope-back" aria-label="Envelope back">
    <svg class="shape" viewBox="0 0 560 280" preserveAspectRatio="none" aria-hidden="true">
      <path class="fill-brown" d="M0,0 L560,0 L280,124 Z"/>
    </svg>
    <div class="wordmark on-dark">Loomvista<span class="dot"></span></div>
  </section>

  <section class="piece letterhead" aria-label="Letterhead">
    <svg class="shape" viewBox="0 0 540 754" preserveAspectRatio="none" aria-hidden="true">
      <path class="fill-blue" d="M0,630 Q270,700 540,630 L540,754 L0,754 Z"/>
      <path d="M0,630 Q270,700 540,630" fill="none" stroke="var(--ink-brown)" stroke-width="5"/>
    </svg>
    <div class="wordmark">Loomvista<span class="dot"></span></div>
    <p class="contact on-blue address">248 Mercer Street<br>Brooklyn, NY 11201</p>
    <p class="contact on-blue reach">646-555-0142<br>contact@loomvista-example.com</p>
  </section>

</main>
</body>
</html>
```